Surface Protection company needs cards

We are a New Zealand company that will apply nanotechnology coatings on surfaces to prevent growth and spread of bacteria, viruses, mold etc with a sprayer. We deal with large corporates, airlines, hospitals and schools so we are after a new modern, simple and clean look that will have great visual impact.
We a company that is focused on prevention and protection.

Company name, Vela Shield

Subtext, Antimicrobial Surface Protection

Logo, VS

Target Market(s)

Hospitals, Transport agencies, Airlines, Corporate entities

Contact Information for Business Card

Company name, VelaShield
Logo, VS

Gareth Tolley
velashieldnz@postbox.example
+64219305562
www.velashield.example.nz

Requirements
Must have
• Simple clean look.
Nice to have
• We apply nano coatings so try and incorporate this into a theme somehow

```html
<!DOCTYPE html>
<html lang="en">
<head>
<meta charset="utf-8">
<title>VelaShield Business Cards</title>
<link rel="stylesheet" href="https://fonts.googleapis.com/css2?family=Montserrat:wght@400;500;700&display=swap">
<style>
  :root {
    --bg: #d9d8d6;
    --card: #262626;
    --accent: #e3222b;
    --ink: #ffffff;
    --muted: #8a8a8a;
    --rule: #9a9a9a;
  }
  * { box-sizing: border-box; margin: 0; padding: 0; }
  html, body {
    width: 1200px; height: 884px; overflow: hidden;
    background: linear-gradient(160deg, #e6e5e3 0%, var(--bg) 60%, #c9c8c6 100%);
    font-family: "Montserrat", sans-serif;
  }
  .canvas {
    width: 1200px; height: 884px;
    display: flex; flex-direction: column; align-items: center; justify-content: center;
    gap: 56px;
  }
  .card {
    width: 620px; height: 354px;
    background: var(--card);
    box-shadow: 0 3px 0 var(--accent), 0 18px 30px rgba(0,0,0,.25);
    position: relative;
    color: var(--ink);
  }

  /* front */
  .card--front { display: flex; align-items: center; }
  .brand {
    width: 310px; padding-left: 40px;
    display: flex; flex-direction: column; align-items: flex-start;
  }
  .brand__row { display: flex; align-items: center; gap: 12px; }
  .brand__dot {
    width: 26px; height: 26px; border-radius: 50%;
    border: 3px solid var(--accent);
  }
  .brand__name {
    font-weight: 700; font-size: 29px; letter-spacing: 1px; color: var(--ink);
    text-transform: uppercase;
  }
  .brand__tagline {
    margin-top: 6px; font-size: 10.5px; letter-spacing: 1.2px;
    color: var(--accent); text-transform: uppercase;
  }
  .divider { width: 1px; height: 150px; background: var(--rule); }
  .contact { padding-left: 30px; }
  .contact__name {
    color: var(--accent); font-weight: 700; font-size: 22px;
    text-transform: uppercase; letter-spacing: .5px;
  }
  .contact__role { font-size: 15px; margin-top: 2px; margin-bottom: 18px; }
  .contact__list { list-style: none; }
  .contact__item {
    display: flex; align-items: center; gap: 10px;
    font-size: 14px; line-height: 24px;
  }
  .contact__icon { width: 14px; height: 14px; flex: none; }

  /* back */
  .card--back {
    display: flex; flex-direction: column; align-items: center; justify-content: center;
  }
  .mark { display: flex; flex-direction: column; align-items: flex-start; }
  .mark__row { display: flex; align-items: center; gap: 16px; }
  .mark__dot { width: 40px; height: 40px; border-radius: 50%; border: 3px solid #555; }
  .mark__name {
    font-weight: 500; font-size: 44px; letter-spacing: 2px; color: var(--muted);
    text-transform: uppercase;
  }
  .mark__tagline {
    margin-top: 4px; margin-left: 56px; font-size: 12px; letter-spacing: 1.6px;
    color: #6e6e6e; text-transform: uppercase;
  }
  .card__web {
    position: absolute; bottom: 46px; left: 0; right: 0; text-align: center;
    font-weight: 500; font-size: 17px; letter-spacing: 1.5px;
  }
</style>
</head>
<body>
<main class="canvas">
  <section class="card card--front">
    <div class="brand">
      <div class="brand__row">
        <span class="brand__dot"></span>
        <span class="brand__name">VelaShield</span>
      </div>
      <p class="brand__tagline">Antimicrobial Surface Protection</p>
    </div>
    <div class="divider"></div>
    <div class="contact">
      <h1 class="contact__name">Gareth Tolley</h1>
      <p class="contact__role">President</p>
      <ul class="contact__list">
        <li class="contact__item">
          <svg class="contact__icon" viewBox="0 0 16 16" aria-hidden="true"><path fill="#e3222b" d="M3.6 1.5l2.2 2.7-1.3 1.6c.9 2 2.6 3.7 4.6 4.6l1.6-1.3 2.7 2.2-1.2 2.2C7 13.3 2.7 9 1.3 2.7z"/></svg>
          +64219305562
        </li>
        <li class="contact__item">
          <svg class="contact__icon" viewBox="0 0 16 16" aria-hidden="true"><rect x="1" y="3" width="14" height="10" fill="#e3222b"/><path d="M1.5 3.5L8 9l6.5-5.5" fill="none" stroke="#262626" stroke-width="1.3"/></svg>
          velashieldnz@postbox.example
        </li>
        <li class="contact__item">
          <svg class="contact__icon" viewBox="0 0 16 16" aria-hidden="true"><circle cx="8" cy="8" r="7" fill="#e3222b"/><path d="M1 8h14M8 1c-3 3.5-3 10.5 0 14M8 1c3 3.5 3 10.5 0 14" fill="none" stroke="#262626" stroke-width="1"/></svg>
          www.velashield.example.nz
        </li>
      </ul>
    </div>
  </section>

  <section class="card card--back">
    <div class="mark">
      <div class="mark__row">
        <span class="mark__dot"></span>
        <span class="mark__name">VelaShield</span>
      </div>
      <p class="mark__tagline">Antimicrobial Surface Protection</p>
    </div>
    <p class="card__web">www.velashield.example.nz</p>
  </section>
</main>
</body>
</html>
```